I will ask the design of the business card

We are looking for business card design of the new company "VORTELL PAYWORKS STUDIO LLC." Based in Azerbaijan.
In case
We are working on Azerbaijan to set up the first exchange of crypto currencies.

The key currency used in exchanges is called "MIRTA".
In case
We are doing project to make crypto currency infrastructure.

We provide state-of-the-art technology to the world.

```html
<!DOCTYPE html>
<html lang="en">
<head>
<meta charset="utf-8">
<title>Vortell Payworks Studio LLC. — Business Card</title>
<link href="https://fonts.googleapis.com/css2?family=Share+Tech+Mono&display=swap" rel="stylesheet">
<style>
  :root {
    --bg: #b9bcc1;
    --red: #d71920;
    --red-deep: #9e1016;
    --red-dark: #6e0c12;
    --red-warm: #e2452a;
    --paper: #ffffff;
    --ink: #1c1c1c;
    --light: #ffffff;
  }
  * { box-sizing: border-box; margin: 0; padding: 0; }
  html, body {
    width: 1200px; height: 857px; overflow: hidden;
    background: var(--bg);
    font-family: "Share Tech Mono", monospace;
  }
  .sheet {
    width: 1200px; height: 857px;
    display: flex; align-items: center; justify-content: center; gap: 48px;
  }
  .card {
    position: relative;
    width: 530px; height: 303px;
    overflow: hidden;
    background: var(--paper);
    box-shadow: 0 6px 18px rgba(0,0,0,0.18);
  }
  .marble {
    position: absolute; top: 0; left: 0; height: 100%;
    background:
      radial-gradient(ellipse 40% 35% at 70% 40%, var(--red-dark) 0%, transparent 70%),
      radial-gradient(ellipse 45% 40% at 20% 80%, var(--red-warm) 0%, transparent 70%),
      radial-gradient(ellipse 50% 45% at 35% 25%, var(--red-deep) 0%, transparent 75%),
      linear-gradient(135deg, var(--red) 0%, var(--red-deep) 55%, var(--red-warm) 100%);
  }
  .card--front .marble { width: 100%; }
  .card--back .marble { width: 44%; }
  .emblem-disc {
    position: absolute;
    border-radius: 50%;
    background: rgba(120, 10, 18, 0.35);
    border: 1px solid rgba(255,255,255,0.25);
  }
  .card--front .emblem-disc { width: 230px; height: 230px; left: 150px; top: 20px; }
  .card--back .emblem-disc { width: 180px; height: 180px; left: 25px; top: 62px; }
  .wordmark {
    position: absolute; color: var(--light);
    letter-spacing: 2px; text-align: center;
  }
  .card--front .wordmark { left: 150px; width: 230px; top: 116px; font-size: 34px; }
  .card--back .wordmark { left: 25px; width: 180px; top: 138px; font-size: 24px; }
  .front-name {
    position: absolute; left: 0; right: 0; bottom: 26px;
    text-align: center; color: var(--light);
    font-size: 19px; letter-spacing: 1px;
  }
  .info {
    position: absolute; left: 48%; right: 14px; top: 52px;
  }
  .info-name {
    color: var(--red); font-size: 21px; font-weight: 400; line-height: 1.05; letter-spacing: 0.5px;
  }
  .info-contact {
    margin-top: 50px; list-style: none;
    color: var(--ink); font-size: 15px; line-height: 1.3; letter-spacing: 0.5px;
  }
  .info-contact .web { color: var(--red); }
</style>
</head>
<body>
<main class="sheet">
  <section class="card card--front">
    <div class="marble" role="img" aria-label="Red fluid-marble artwork background"></div>
    <div class="emblem-disc"></div>
    <div class="wordmark">VORTELL</div>
    <div class="front-name">VORTELL PAYWORKS STUDIO LLC.</div>
  </section>

  <section class="card card--back">
    <div class="marble" role="img" aria-label="Red fluid-marble artwork panel"></div>
    <div class="emblem-disc"></div>
    <div class="wordmark">VORTELL</div>
    <div class="info">
      <h1 class="info-name">VORTELL PAYWORKS<br>STUDIO LLC.</h1>
      <ul class="info-contact">
        <li>CITY, STATE</li>
        <li>+994 12 480 7316</li>
        <li>ANA.ROE@VORTELL.AZ</li>
        <li class="web">WWW.VORTELL.AZ</li>
      </ul>
    </div>
  </section>
</main>
</body>
</html>
```